Business Card Design Project - The Bridgeway Partners

Company Name - The Bridgeway Partners

We need a unique logo and business cards

We are a team of experienced IT professionals who specialize in providing business value to organizations via the analysis and understanding the challenges of your particular organization. We focus on understanding the challenges first, and execute against your priorities partnering with your highly valued key resources.

Our extensive experience and focus on Agile delivery methodologies help our clients continuously improve and deliver quality solutions. Using this approach we will always deliver the greatest return on your investments.

Target Market(s)

Large organizations IT departments

Industry/Entity Type

Business

Font styles to use
Serif
Sans Serif

Requirements
Should not have
• no pictures

```html
<!DOCTYPE html>
<html lang="en">
<head>
<meta charset="utf-8">
<title>The Bridgeway Partners – Business Cards</title>
<link href="https://fonts.googleapis.com/css2?family=Exo+2:wght@400;800&display=swap" rel="stylesheet">
<style>
  :root {
    --page: #e6e8eb;
    --card: #ffffff;
    --card-shade: #eef0f3;
    --brand-navy: #1f4fa6;
    --brand-blue: #2a7fd8;
    --brand-sky: #2fb2ee;
    --ink: #3a3f48;
    --white: #ffffff;
  }
  * { box-sizing: border-box; margin: 0; padding: 0; }
  html, body { width: 1200px; height: 901px; overflow: hidden; }
  body {
    background: var(--page);
    font-family: "Exo 2", sans-serif;
    position: relative;
  }
  .business-card {
    position: absolute;
    top: 170px;
    width: 340px;
    height: 560px;
    border-radius: 24px;
    background: linear-gradient(180deg, var(--card) 0%, var(--card-shade) 100%);
    box-shadow: 0 10px 28px rgba(30, 40, 60, 0.18);
    overflow: hidden;
  }
  .card-front { left: 200px; }
  .card-back { left: 660px; }

  .brand { display: flex; align-items: center; gap: 10px; }
  .brand-dot { border-radius: 50%; background: var(--brand-blue); flex: none; }
  .brand-name {
    font-weight: 800;
    color: var(--brand-navy);
    white-space: nowrap;
  }

  /* front */
  .card-front .brand { position: absolute; left: 24px; top: 40px; }
  .card-front .brand-dot { width: 26px; height: 26px; }
  .card-front .brand-name { font-size: 22px; }

  .person { position: absolute; left: 26px; top: 110px; color: var(--ink); }
  .person-name { font-size: 18px; font-weight: 400; letter-spacing: 2px; }
  .person-title { font-size: 12px; font-weight: 400; margin-top: 3px; letter-spacing: 0.5px; }

  .front-band { position: absolute; left: 0; top: 0; width: 340px; height: 560px; }

  .contact-list {
    position: absolute;
    right: 26px;
    bottom: 30px;
    list-style: none;
    color: var(--white);
    font-size: 12px;
    line-height: 20px;
    text-align: right;
  }
  .contact-list li { display: flex; justify-content: flex-end; align-items: center; gap: 8px; }
  .contact-icon { width: 12px; height: 12px; flex: none; }
  .icon-spacer { width: 12px; flex: none; }

  /* back */
  .card-back .brand {
    position: absolute;
    inset: 0;
    flex-direction: column;
    justify-content: center;
    gap: 18px;
  }
  .card-back .brand-dot { width: 60px; height: 60px; }
  .card-back .brand-name { font-size: 26px; }
</style>
</head>
<body>

<section class="business-card card-front" aria-label="Business card front">
  <svg class="front-band" viewBox="0 0 340 560" aria-hidden="true">
    <defs>
      <radialGradient id="bandGlow" cx="0.5" cy="0.55" r="0.7">
        <stop offset="0" stop-color="#2fb2ee"/>
        <stop offset="0.6" stop-color="#2a7fd8"/>
        <stop offset="1" stop-color="#1f4fa6"/>
      </radialGradient>
    </defs>
    <path d="M0,220 C110,270 230,320 340,300 L340,560 L0,560 Z" fill="url(#bandGlow)"/>
    <path d="M0,210 C110,260 230,310 340,290" fill="none" stroke="#1f4fa6" stroke-width="2"/>
    <path d="M30,255 C130,300 240,340 340,322" fill="none" stroke="#ffffff" stroke-width="3"/>
  </svg>

  <div class="brand">
    <span class="brand-dot"></span>
    <span class="brand-name">The Bridgeway Partners</span>
  </div>

  <div class="person">
    <p class="person-name">DANIEL WHITMORE</p>
    <p class="person-title">Managing Director</p>
  </div>

  <ul class="contact-list">
    <li>412 Harbour Court<span class="icon-spacer"></span></li>
    <li>Kestrel Avenue NW4
      <svg class="contact-icon" viewBox="0 0 12 12"><path d="M6 0.5a3.8 3.8 0 0 0-3.8 3.8C2.2 7.2 6 11.5 6 11.5s3.8-4.3 3.8-7.2A3.8 3.8 0 0 0 6 0.5zm0 5.2a1.4 1.4 0 1 1 0-2.8 1.4 1.4 0 0 1 0 2.8z" fill="#fff"/></svg>
    </li>
    <li>014 555 0182
      <svg class="contact-icon" viewBox="0 0 12 12"><path d="M2.4 0.8l2 2.2-1 1.4c.7 1.6 1.9 2.8 3.4 3.5l1.4-1 2.2 2-1.1 2.2C4.6 11 1 7.4.3 2z" fill="#fff"/></svg>
    </li>
    <li>014 555 0183
      <svg class="contact-icon" viewBox="0 0 12 12"><rect x="2" y="1" width="8" height="10" rx="1" fill="none" stroke="#fff" stroke-width="1.3"/><rect x="4" y="3" width="4" height="1.3" fill="#fff"/></svg>
    </li>
    <li>dan@bridgewaymail.com
      <svg class="contact-icon" viewBox="0 0 12 12"><rect x="0.7" y="2.2" width="10.6" height="7.6" fill="none" stroke="#fff" stroke-width="1.2"/><path d="M0.7 2.4L6 6.6l5.3-4.2" fill="none" stroke="#fff" stroke-width="1.2"/></svg>
    </li>
    <li>www.bridgewaypartners.net
      <svg class="contact-icon" viewBox="0 0 12 12"><circle cx="6" cy="6" r="5" fill="none" stroke="#fff" stroke-width="1.2"/><path d="M1 6h10M6 1c2 2.6 2 7.4 0 10M6 1c-2 2.6-2 7.4 0 10" fill="none" stroke="#fff" stroke-width="1"/></svg>
    </li>
  </ul>
</section>

<section class="business-card card-back" aria-label="Business card back">
  <div class="brand">
    <span class="brand-dot"></span>
    <span class="brand-name">The Bridgeway Partners</span>
  </div>
</section>

</body>
</html>
```